Social Movement/Church Plant Website - KindAshbury.com

We need a website for our church plant startup, however we want the focus of the landing page to be around #kindashbury - that we are an organization that is FOR our town (Ashbury). The site will include serving project events, social events, a place to sign up for emails, a blog, a place to give, etc. All the elements we know we want are currently at kindashbury.com . Please check this for copy.

We want this to be easy to edit as a non-developer.

I have included several logos with our colors, as well as an ai file to give you an idea of how we want the design to look and feel - also includes our branded fonts

Target Market(s)

People who live in the Northern CO area

Font styles to use
Serif
Sans Serif

Requirements
Must have
• Events (serve and social), Blog section, A place to get involved - where to give and to sign up for emails. Must match our branding colors and style hex 4c7991.
Should not have
• Should not be focused on the actual church plant on the home page. There can be some back end stuff about it, but the focus should be #kindashbury.

```html
<!DOCTYPE html>
<html lang="en">
<head>
<meta charset="utf-8">
<title>KindAshbury</title>
<link href="https://fonts.googleapis.com/css2?family=Kaushan+Script&family=Josefin+Sans:wght@300;400;600;700&display=swap" rel="stylesheet">
<style>
:root{
  --brand:#4c7991;
  --brand-dark:#3d6478;
  --ink:#2b2b2b;
  --muted:#6f6f6f;
  --band:#ececec;
  --white:#ffffff;
  --line:#c9c9c9;
}
*{box-sizing:border-box;margin:0;padding:0}
html,body{width:1200px;height:4128px;overflow:hidden}
body{position:relative;background:var(--white);font-family:"Josefin Sans",sans-serif;color:var(--ink)}
.abs{position:absolute}
.script{font-family:"Kaushan Script",cursive;font-weight:400}

/* header */
.site-header{left:0;top:0;width:1200px;height:100px;background:var(--white);z-index:3}
.brand-name{left:100px;top:26px;font-size:34px;font-weight:700;color:var(--ink);letter-spacing:.5px}
.main-nav{right:100px;top:30px;display:flex;gap:24px;font-size:16px;color:var(--ink)}
.social-dots{right:100px;top:62px;display:flex;gap:12px}
.social-dots span{width:12px;height:12px;border-radius:50%;background:var(--ink)}

/* hero */
.hero{left:0;top:100px;width:1200px;height:600px;background:linear-gradient(120deg,#5d6b73 0%,#8a7a64 40%,#b69a7b 60%,#56636e 100%)}
.hero-title{left:0;top:290px;width:1200px;text-align:center;font-family:"Josefin Sans",sans-serif;font-weight:700;font-size:84px;line-height:1;color:var(--white);letter-spacing:1px}
.hero-btn{left:510px;top:418px;width:180px;height:50px;border:2px solid var(--white);color:var(--white);font-size:18px;display:flex;align-items:center;justify-content:center}
.torn-edge{left:0;top:640px;width:1200px;height:70px}

/* story */
.story-photo{left:120px;top:790px;width:230px;height:230px;border-radius:50%;background:radial-gradient(circle at 40% 40%,#9bb07d,#5d7a4c 60%,#3f5a38)}
.story-title{left:560px;top:770px;font-size:44px;line-height:1.2}
.story-sub{left:560px;top:842px;font-size:22px;color:var(--ink)}
.story-text{left:560px;top:886px;width:520px;font-size:15px;line-height:1.6;color:var(--muted);font-style:italic}
.btn{display:flex;align-items:center;justify-content:center;font-size:16px;height:42px}
.btn-outline{border:2px solid var(--ink);color:var(--ink)}
.btn-fill{background:var(--brand);color:var(--white)}
.story-read{left:560px;top:1030px;width:120px}
.story-contact{left:720px;top:1030px;width:140px}

/* bands */
.band{left:0;background:var(--band)}
.band-edge{left:0;width:1200px;height:40px}
.section-title{left:0;width:1200px;text-align:center;font-size:44px;color:var(--ink)}

/* project events */
.project-card{top:1400px;width:330px;height:260px;background:var(--white);box-shadow:0 2px 6px rgba(0,0,0,.08)}
.project-photo{width:330px;height:200px}
.project-label{height:60px;display:flex;align-items:center;justify-content:space-between;padding:0 18px;font-weight:700;font-size:17px}
.project-label i{width:16px;height:16px;border-radius:50%;background:var(--ink);display:block}
.projects-btn{left:525px;top:1700px;width:150px;height:40px;font-size:15px}

/* mailing */
.mail-field{top:2030px;height:44px;border:1px solid var(--line);padding:0 12px;display:flex;align-items:center;font-size:15px;color:var(--muted)}
.mail-submit{left:975px;top:2030px;width:125px;height:44px;font-size:16px}

/* social events */
.social-bg{left:0;top:2170px;width:1200px;height:800px;background:linear-gradient(180deg,#f3f3f3,#e6e6e6)}
.social-tile{box-shadow:0 2px 6px rgba(0,0,0,.08)}

/* blog */
.timeline{left:599px;top:3100px;width:2px;height:500px;background:var(--line)}
.timeline-dot{left:588px;width:24px;height:24px;border-radius:50%;background:var(--brand);border:4px solid var(--band)}
.blog-card{width:400px;height:220px;background:var(--white);display:flex;padding:20px;gap:18px;box-shadow:0 2px 6px rgba(0,0,0,.08)}
.blog-photo{width:170px;height:130px;flex:none}
.blog-body h3{font-size:17px;font-weight:700;line-height:1.3;margin-bottom:10px}
.blog-body p{font-size:13px;line-height:1.5;color:var(--muted);margin-bottom:10px}
.blog-body a{font-size:13px;color:var(--brand);text-decoration:none}

/* footer */
.footer-col h4{font-size:17px;font-weight:700;color:var(--brand);margin-bottom:18px;letter-spacing:.5px}
.footer-col p{font-size:13px;line-height:1.7;color:var(--muted)}
.footer-col ul{list-style:none;font-size:13px;line-height:1.9;color:var(--muted)}
.footer-col li span{display:inline-block;width:8px;height:8px;border-radius:50%;background:var(--brand);margin-right:8px}
.copyright{left:0;top:4080px;width:1200px;height:48px;border-top:1px solid var(--line);text-align:center;line-height:48px;font-size:13px;color:var(--muted)}
.copyright b{color:var(--brand);font-weight:600}
</style>
</head>
<body>

<header class="site-header abs">
  <div class="brand-name abs">#KindAshbury</div>
  <nav class="main-nav abs"><span>Home</span><span>About</span><span>Events</span><span>Blog</span><span>Give</span><span>Contact Us</span></nav>
  <div class="social-dots abs"><span></span><span></span><span></span></div>
</header>

<section class="hero abs" role="img" aria-label="Photo of friends sharing food outdoors in town"></section>
<div class="hero-title abs">#KindAshbury</div>
<div class="hero-btn abs">Learn more</div>
<svg class="torn-edge abs" viewBox="0 0 1200 70" preserveAspectRatio="none"><path d="M0 40 L60 30 L120 45 L200 28 L280 42 L360 26 L440 44 L520 30 L600 46 L680 27 L760 43 L840 29 L920 45 L1000 28 L1080 42 L1140 30 L1200 38 L1200 70 L0 70Z" fill="#fff"/></svg>

<section>
  <div class="story-photo abs" role="img" aria-label="Photo of volunteers planting a community garden"></div>
  <h2 class="story-title abs script">Our Story</h2>
  <div class="story-sub abs">Working Toward a Better Tomorrow</div>
  <p class="story-text abs">What if we were known not by what we're against, but by what we're for? If our collective energy was invested in things that unite rather than divide, wouldn't we see stronger neighborhoods, healthier communities and more resilient relationships? We believe so.</p>
  <div class="btn btn-outline story-read abs">Read More</div>
  <div class="btn btn-fill story-contact abs">Contact Now</div>
</section>

<section>
  <svg class="band-edge abs" style="top:1180px" viewBox="0 0 1200 40" preserveAspectRatio="none"><path d="M0 30 Q150 10 300 24 T600 20 T900 26 T1200 18 L1200 40 L0 40Z" fill="#ececec"/></svg>
  <div class="band abs" style="top:1219px;width:1200px;height:600px"></div>
  <svg class="band-edge abs" style="top:1818px" viewBox="0 0 1200 40" preserveAspectRatio="none"><path d="M0 0 L1200 0 L1200 14 Q900 30 600 16 T0 22Z" fill="#ececec"/></svg>
  <h2 class="section-title abs script" style="top:1300px">Project Events</h2>
  <div class="project-card abs" style="left:100px"><div class="project-photo" role="img" aria-label="Photo of volunteers sorting donations" style="background:linear-gradient(135deg,#9fc0c8,#5f8a6e)"></div><div class="project-label">CLEANUP<i></i></div></div>
  <div class="project-card abs" style="left:435px"><div class="project-photo" role="img" aria-label="Photo of volunteers cleaning a school field" style="background:linear-gradient(135deg,#6f8f4a,#3d5a30)"></div><div class="project-label">SCHOOL CLEANUP<i></i></div></div>
  <div class="project-card abs" style="left:770px"><div class="project-photo" role="img" aria-label="Photo of a team building a gaga pit" style="background:linear-gradient(135deg,#8a6a52,#4e3a2c)"></div><div class="project-label">BUILDING GAGA<i></i></div></div>
  <div class="btn btn-fill projects-btn abs">View All Projects</div>
</section>

<section>
  <h2 class="section-title abs script" style="top:1920px;font-size:40px">Join our mailing list &amp; stay updated!</h2>
  <div class="mail-field abs" style="left:100px;width:425px">Name</div>
  <div class="mail-field abs" style="left:535px;width:430px">Email</div>
  <div class="btn btn-fill mail-submit abs">Subscribe</div>
</section>

<section>
  <div class="social-bg abs"></div>
  <h2 class="section-title abs script" style="top:2260px">Social Events</h2>
  <div class="social-tile abs" role="img" aria-label="Photo of neighbors building a garden bed" style="left:110px;top:2360px;width:335px;height:410px;background:linear-gradient(180deg,#8fb4d6 0%,#a99072 45%,#6b5a44 100%)"></div>
  <div class="social-tile abs" role="img" aria-label="Photo of friends gardening together" style="left:460px;top:2360px;width:315px;height:200px;background:linear-gradient(135deg,#6f8c55,#3e5632)"></div>
  <div class="social-tile abs" role="img" aria-label="Photo of a water park on a sunny day" style="left:790px;top:2360px;width:310px;height:200px;background:linear-gradient(180deg,#7fb0dc,#6e9a5c)"></div>
  <div class="social-tile abs" role="img" aria-label="Photo of a smiling group at an event" style="left:460px;top:2570px;width:315px;height:200px;background:linear-gradient(135deg,#c49a78,#6e5040)"></div>
  <div class="social-tile abs" role="img" aria-label="Photo of a bounce house in a park" style="left:790px;top:2570px;width:310px;height:200px;background:linear-gradient(180deg,#6fa6d8,#7ca35b)"></div>
</section>

<section>
  <div class="band abs" style="top:2970px;width:1200px;height:760px"></div>
  <svg class="band-edge abs" style="top:3729px" viewBox="0 0 1200 40" preserveAspectRatio="none"><path d="M0 0 L1200 0 L1200 18 Q900 32 600 14 T0 24Z" fill="#ececec"/></svg>
  <h2 class="section-title abs script" style="top:2985px">Latest Blog</h2>
  <div class="timeline abs"></div>
  <div class="timeline-dot abs" style="top:3190px"></div>
  <div class="timeline-dot abs" style="top:3470px"></div>

  <article class="blog-card abs" style="left:120px;top:3090px"><div class="blog-photo" role="img" aria-label="Photo of a man sharing a meal" style="background:linear-gradient(135deg,#b58a6c,#5e4536)"></div><div class="blog-body"><h3>AT VERO EOS ET ACCUSAMUS ET</h3><p>Sed ut perspiciatis unde omnis iste natus error sit voluptatem.</p><a>Read More</a></div></article>
  <article class="blog-card abs" style="left:700px;top:3090px"><div class="blog-photo" role="img" aria-label="Photo of neighbors in a garden" style="background:linear-gradient(135deg,#8fb26a,#4d6b3b)"></div><div class="blog-body"><h3>AT VERO EOS ET ACCUSAMUS ET</h3><p>Sed ut perspiciatis unde omnis iste natus error sit voluptatem.</p><a>Read More</a></div></article>
  <article class="blog-card abs" style="left:120px;top:3370px"><div class="blog-photo" role="img" aria-label="Photo of a volunteer at work" style="background:linear-gradient(135deg,#7a6a52,#3e3428)"></div><div class="blog-body"><h3>AT VERO EOS ET ACCUSAMUS ET</h3><p>Sed ut perspiciatis unde omnis iste natus error sit voluptatem.</p><a>Read More</a></div></article>
  <article class="blog-card abs" style="left:700px;top:3370px"><div class="blog-photo" role="img" aria-label="Photo of a group outdoors" style="background:linear-gradient(135deg,#9bbad0,#5d7a5a)"></div><div class="blog-body"><h3>AT VERO EOS ET ACCUSAMUS ET</h3><p>Sed ut perspiciatis unde omnis iste natus error sit voluptatem.</p><a>Read More</a></div></article>
</section>

<footer>
  <div class="footer-col abs" style="left:100px;top:3820px;width:340px">
    <h4>KIND ASHBURY</h4>
    <p>Sed ut perspiciatis unde omnis iste natus error sit voluptatem accusantium doloremque laudantium, totam rem aperiam, eaque ipsa quae ab illo inventore veritatis et quasi architecto beatae vitae dicta sunt explicabo nemo enim ipsam.</p>
  </div>
  <div class="footer-col abs" style="left:545px;top:3820px">
    <h4>QUICK LINK</h4>
    <ul><li>Home</li><li>About</li><li>Events</li><li>Blog</li><li>Give</li><li>Contact Us</li></ul>
  </div>
  <div class="footer-col abs" style="left:740px;top:3820px">
    <h4>INSIGHTS</h4>
    <ul><li>News of Projects</li><li>Press Center</li><li>How We Partner</li><li>Webinars &amp; Events</li><li>Newsletter Sign up</li></ul>
  </div>
  <div class="footer-col abs" style="left:955px;top:3820px">
    <h4>GET CONNECTED</h4>
    <ul><li><span></span>Photos</li><li><span></span>Updates</li><li><span></span>Community</li><li><span></span>Network</li><li><span></span>Videos</li></ul>
  </div>
  <div class="copyright abs">© 2024 Copyright <b>KindAshbury</b> All Rights Reserved</div>
</footer>

</body>
</html>
```